Business Cards and stationery for Bright Harbor Fixtures, LLC
Say farewell to stray grit
Professional
Delphine M. Carraway
President
517 Maplebrook Lane
Colchester, CT 06492
USA
delphine@clearveil.example
www.clearveil.example
Logo should match the one being designed in this overall brief

```html
<!DOCTYPE html>
<html lang="en">
<head>
<meta charset="utf-8">
<title>Bright Harbor Fixtures — Stationery Set</title>
<link rel="stylesheet" href="https://fonts.googleapis.com/css2?family=Montserrat:wght@400;800&family=Open+Sans:wght@400;600&display=swap">
<style>
  :root {
    --backdrop: #9b9b9b;
    --paper: #ffffff;
    --green: #8cc63f;
    --charcoal: #3b3b3d;
    --ink: #555555;
    --shadow: 0 3px 8px rgba(0,0,0,0.25);
  }
  * { margin: 0; padding: 0; box-sizing: border-box; }
  html, body { width: 1200px; height: 949px; overflow: hidden; }
  body {
    position: relative;
    background: var(--backdrop);
    font-family: "Open Sans", Arial, sans-serif;
    color: var(--ink);
  }
  .piece { position: absolute; background: var(--paper); box-shadow: var(--shadow); overflow: hidden; }
  .swoosh { position: absolute; left: 0; bottom: 0; width: 100%; display: block; }
  .wordmark {
    font-family: "Montserrat", Arial, sans-serif;
    font-weight: 800;
    text-transform: uppercase;
    line-height: 0.95;
    color: var(--charcoal);
    text-align: center;
    letter-spacing: 0.02em;
  }
  .address { font-size: 7px; line-height: 1.4; text-align: left; }

  /* corner brand mark */
  .brand-corner { position: absolute; left: 943px; top: 22px; width: 175px; color: var(--paper); font-size: 30px; }

  /* letterhead */
  .letterhead { left: 38px; top: 46px; width: 467px; height: 651px; }
  .letterhead .wordmark-top { position: absolute; left: 26px; top: 22px; font-size: 17px; text-align: left; }
  .letterhead .address { position: absolute; right: 28px; top: 26px; font-size: 6.5px; }
  .letterhead .wordmark-faint { position: absolute; left: 0; right: 0; top: 250px; font-size: 70px; color: var(--charcoal); opacity: 0.08; }
  .letterhead .swoosh { height: 150px; }

  /* disc sleeve */
  .sleeve { left: 551px; top: 136px; width: 316px; height: 318px; }
  .sleeve .notch { position: absolute; right: -40px; top: 90px; width: 80px; height: 130px; border-left: 1px solid #d8d8d8; border-radius: 50%; }
  .sleeve .wordmark { position: absolute; left: 70px; top: 125px; font-size: 30px; text-align: left; }
  .sleeve .swoosh { height: 90px; }

  /* disc */
  .disc { position: absolute; left: 900px; top: 131px; width: 318px; height: 318px; }
  .disc .wordmark { position: absolute; left: 70px; top: 57px; width: 180px; color: var(--paper); font-size: 26px; }

  /* envelope */
  .envelope { left: 615px; top: 610px; width: 534px; height: 295px; }
  .envelope .flap { position: absolute; left: 0; top: 0; width: 100%; height: 58px; background: var(--green); }
  .envelope .wordmark { position: absolute; left: 180px; top: 125px; font-size: 34px; text-align: left; }
  .envelope .address { position: absolute; left: 405px; top: 148px; font-size: 6.5px; }
  .envelope .swoosh { height: 100px; }

  /* business cards */
  .card { top: 759px; width: 246px; height: 144px; }
  .card-back { left: 36px; }
  .card-front { left: 331px; top: 767px; width: 243px; height: 138px; }
  .card-back .contact { position: absolute; left: 14px; top: 14px; font-size: 5.5px; line-height: 1.45; }
  .card-back .contact .name { font-size: 7px; font-weight: 600; color: var(--charcoal); }
  .card-back .contact .spacer { height: 8px; }
  .card-back .wordmark { position: absolute; right: 24px; top: 40px; font-size: 15px; text-align: left; }
  .card-front .wordmark { position: absolute; left: 0; right: 0; top: 50px; font-size: 16px; }
  .card .swoosh { height: 48px; }
</style>
</head>
<body>

  <div class="wordmark brand-corner">Bright<br>Harbor</div>

  <section class="piece letterhead" aria-label="Letterhead">
    <div class="wordmark wordmark-top">Bright<br>Harbor</div>
    <address class="address" style="font-style:normal">517 Maplebrook Lane<br>Colchester, CT 06492</address>
    <div class="wordmark wordmark-faint" aria-hidden="true">Bright<br>Harbor</div>
    <svg class="swoosh" viewBox="0 0 400 150" preserveAspectRatio="none" aria-hidden="true">
      <path d="M0 60 C120 110 260 110 400 75 L400 150 L0 150 Z" fill="var(--green)"/>
      <path d="M0 88 C140 128 280 122 400 88 L400 150 L0 150 Z" fill="var(--paper)"/>
      <path d="M150 150 C260 140 340 118 400 92 L400 150 Z" fill="var(--charcoal)"/>
    </svg>
  </section>

  <section class="piece sleeve" aria-label="Disc sleeve">
    <div class="notch"></div>
    <div class="wordmark">Bright<br>Harbor</div>
    <svg class="swoosh" viewBox="0 0 300 90" preserveAspectRatio="none" aria-hidden="true">
      <path d="M0 20 C90 60 200 62 300 35 L300 90 L0 90 Z" fill="var(--green)"/>
      <path d="M0 48 C100 80 210 76 300 48 L300 90 L0 90 Z" fill="var(--paper)"/>
      <path d="M100 90 C190 84 250 70 300 52 L300 90 Z" fill="var(--charcoal)"/>
    </svg>
  </section>

  <div class="disc" aria-label="Disc label">
    <svg width="318" height="318" viewBox="0 0 318 318" aria-hidden="true">
      <defs><clipPath id="disc-face"><circle cx="159" cy="159" r="159"/></clipPath></defs>
      <g clip-path="url(#disc-face)">
        <rect width="318" height="159" fill="var(--green)"/>
        <rect y="159" width="318" height="159" fill="var(--charcoal)"/>
      </g>
      <circle cx="159" cy="159" r="34" fill="#e6e6e6"/>
      <circle cx="159" cy="159" r="24" fill="var(--backdrop)"/>
    </svg>
    <div class="wordmark">Bright<br>Harbor</div>
  </div>

  <section class="piece envelope" aria-label="Envelope">
    <div class="flap"></div>
    <div class="wordmark">Bright<br>Harbor</div>
    <address class="address" style="font-style:normal">517 Maplebrook Lane<br>Colchester, CT 06492</address>
    <svg class="swoosh" viewBox="0 0 500 100" preserveAspectRatio="none" aria-hidden="true">
      <path d="M0 20 C150 70 330 72 500 35 L500 100 L0 100 Z" fill="var(--green)"/>
      <path d="M0 50 C170 92 340 86 500 50 L500 100 L0 100 Z" fill="var(--paper)"/>
      <path d="M180 100 C320 92 420 75 500 55 L500 100 Z" fill="var(--charcoal)"/>
    </svg>
  </section>

  <section class="piece card card-back" aria-label="Business card, contact side">
    <div class="contact">
      <div class="name">Delphine M. Carraway</div>
      <div>President</div>
      <div class="spacer"></div>
      <div>517 Maplebrook Lane</div>
      <div>Colchester, CT 06492, USA</div>
      <div>delphine@clearveil.example</div>
      <div>www.clearveil.example</div>
    </div>
    <div class="wordmark">Bright<br>Harbor</div>
    <svg class="swoosh" viewBox="0 0 250 48" preserveAspectRatio="none" aria-hidden="true">
      <path d="M0 8 C80 32 170 32 250 14 L250 48 L0 48 Z" fill="var(--green)"/>
      <path d="M0 26 C90 46 180 42 250 24 L250 48 L0 48 Z" fill="var(--paper)"/>
      <path d="M90 48 C170 44 220 36 250 27 L250 48 Z" fill="var(--charcoal)"/>
    </svg>
  </section>

  <section class="piece card card-front" aria-label="Business card, brand side">
    <div class="wordmark">Bright<br>Harbor</div>
    <svg class="swoosh" viewBox="0 0 250 48" preserveAspectRatio="none" aria-hidden="true">
      <path d="M0 8 C80 32 170 32 250 14 L250 48 L0 48 Z" fill="var(--green)"/>
      <path d="M0 26 C90 46 180 42 250 24 L250 48 L0 48 Z" fill="var(--paper)"/>
      <path d="M90 48 C170 44 220 36 250 27 L250 48 Z" fill="var(--charcoal)"/>
    </svg>
  </section>

</body>
</html>
```